K7 Teaser

One page teaser for our business information and model. A financial service SPV platform.

Target Market(s)

Financial Professionals

Industry/Entity Type

Financial Service

Font styles to use
Sans Serif

Colors
ffcf3e
ffffff
cfcfcf
9d9d9d
aaaaaa
fbed22
ffc214
fee18a
fbee3f

Requirements
Must have
• Unique appearance of USPs.
• Important claims: Low Cost. First Class.
• and: We liberate the buy-side from the sell-side
Nice to have
• maybe keyword cloud

```html
<!DOCTYPE html>
<html lang="en">
<head>
<meta charset="utf-8">
<title>K7 Teaser</title>
<link href="https://fonts.googleapis.com/css2?family=Open+Sans:wght@300;400;600;700;800&family=Roboto+Condensed:wght@400&display=swap" rel="stylesheet">
<style>
  :root{
    --gold:#c9973a;
    --gold-text:#d29a2c;
    --cream:#f5e7d5;
    --grey-dark:#595959;
    --ink:#111;
    --body-ink:#333;
    --white:#ffffff;
    --page-bg:#e6e6e6;
  }
  *{margin:0;padding:0;box-sizing:border-box}
  html,body{width:1200px;height:1200px;overflow:hidden;background:var(--page-bg)}
  body{font-family:"Open Sans",Arial,sans-serif;position:relative}
  .flyer{position:absolute;left:194px;top:25px;width:938px;height:1328px;background:var(--white);
    transform:scale(0.866);transform-origin:0 0;overflow:hidden}

  .hero{position:absolute;left:0;top:0;width:938px;height:497px;
    background:linear-gradient(100deg,#8a7a3a 0%,#6f7a55 35%,#4c8a8a 65%,#2f6a7c 100%)}
  .hero-photo{position:absolute;inset:0}
  .headline{position:absolute;left:86px;width:480px;top:116px;text-align:center;color:var(--white);
    font-weight:800;font-size:70px;line-height:71px;letter-spacing:-0.5px}

  .intro{position:absolute;left:0;top:497px;width:938px;height:469px;
    background:linear-gradient(90deg,#c4c4c6 0%,#e9e9ea 40%,#ffffff 60%)}
  .intro-copy{position:absolute;left:96px;top:553px;width:376px;font-weight:300;font-size:15.6px;
    line-height:25.3px;color:var(--body-ink)}

  .claim{position:absolute;left:502px;top:552px;width:400px;text-align:center;color:var(--grey-dark);
    font-weight:600;font-size:36px;line-height:37px}

  .usp-box{position:absolute;left:502px;top:688px;width:400px;height:278px;background:var(--cream);
    border-radius:40px 40px 0 0}
  .usp-col{position:absolute;top:30px;width:200px;text-align:center;font-weight:700;font-size:13.8px;line-height:16px}
  .usp-col.left{left:8px}
  .usp-col.right{left:196px}
  .usp-col p{margin-bottom:9px}
  .usp-col .accent{color:var(--gold-text)}
  .usp-col .plain{color:var(--ink)}

  .price-band{position:absolute;left:0;top:966px;width:938px;height:86px;background:var(--gold);
    color:var(--white);font-family:"Roboto Condensed",Arial,sans-serif;font-size:18px;line-height:23px;
    text-align:center;padding-top:19px}

  .keyword-panel{position:absolute;left:0;top:1052px;width:287px;height:170px;background:var(--gold);
    border-radius:0 0 40px 0}

  .brand-name{position:absolute;left:287px;width:651px;top:1110px;text-align:center;
    font-weight:400;font-size:36px;letter-spacing:2px;color:var(--gold)}
  .tagline{position:absolute;left:287px;width:651px;top:1199px;text-align:center;color:var(--gold);
    font-weight:600;font-size:16.5px;letter-spacing:4.3px}

  .contact{position:absolute;left:0;width:938px;top:1236px;text-align:center;font-weight:600;font-size:14px;color:var(--ink)}
  .about{position:absolute;left:0;width:938px;top:1262px;text-align:center;font-size:11.5px;line-height:15px;color:var(--body-ink)}
</style>
</head>
<body>
<main class="flyer">
  <section class="hero">
    <div class="hero-photo" role="img" aria-label="City skyline overlaid with a world map, candlestick chart and a rising arrow"></div>
    <h1 class="headline">Liberating<br>the buy-side<br>from the<br>sell-side</h1>
  </section>

  <section class="intro"></section>
  <p class="intro-copy">We serve our clients with the power to create their own branded, tailor-made financial products and investment solutions by providing them with right tools and structures to establish and operate first class off-balance sheet issuance vehicles (SPV). We create unique solutions to expand your business reach, services and qualities by liberating financial product issuance to buy-side. Asset owners, distributers and managers are given the full capability to securitise their own asset base in unlimited capacity, outside their balance sheet with customisable transparency and counterparty risk. A clear and simple solution to serve your best interests and without the need for conventional sell-side issuers.</p>

  <h2 class="claim">We democratise structured financial product issuance</h2>

  <div class="usp-box">
    <div class="usp-col left">
      <p class="accent">Off-balance sheet</p>
      <p class="plain">Own issuance vehicle<br>(SPV)</p>
      <p class="accent">Regulatory compliant<br>(MIFID)</p>
      <p class="plain">Swiss Paying Agent</p>
      <p class="accent">Various<br>off-shore locations</p>
      <p class="plain">Open Architecture</p>
      <p class="accent">Daily Liquidity</p>
    </div>
    <div class="usp-col right">
      <p class="accent">Customised<br>Transparency</p>
      <p class="plain">Low cost structure</p>
      <p class="accent">Your own fee policy</p>
      <p class="plain">Investment<br>&amp; risk control</p>
      <p class="accent">Quick setup</p>
      <p class="plain">Transparent<br>secondary market</p>
      <p class="accent">Full transparent pricing</p>
    </div>
  </div>

  <div class="price-band">
    Establishment Cost CHF 20’000 &nbsp; | &nbsp; Recurring Cost Yearly 20 BPS (&gt; CHF 20’000) &nbsp; | &nbsp; Product Cost&nbsp; CHF 2’000<br>
    Ticket Fee for Adjustments, Corporate Actions &amp; Rebalancing &nbsp;- &nbsp;Documentation Standard Set inkl. KID
  </div>

  <div class="keyword-panel" role="img" aria-label="Keyword cloud of structured product terms such as securitisation, leverage products and trackers"></div>

  <p class="brand-name">NORVANE FINANCIAL PRODUCTS</p>
  <p class="tagline">YOUR BRAND. YOUR REWARD. YOUR SOLUTION.</p>

  <p class="contact">Norvane Financial Products AG &nbsp;I&nbsp; Lindenweg 14 &nbsp;I&nbsp; CH-8002 Zürich &nbsp;I&nbsp; www.norvanefp.com &nbsp;I&nbsp; +41 44 000 12 34</p>
  <p class="about">Norvane Financial Product AG is a financial service provider built on the unique experience and robust track record<br>of its team. Our founders gathered the most qualified experts to benefit our clients and business partners.</p>
</main>
</body>
</html>
```